Hexagon Honey Bottle Design, simple and elegant.

Bottle description:
BODY HEIGHT With cap 8.75cm
Without cap 8.6cm
DIAMETER Inner 4.4cm
Outer 5.2cm
Label height only has to be = 6cm height x (3.4X6) length of one hexagonal box is 3.4cm
See through bottle with black cap.
Concept of design:
Elegant, Simple, no pictures of bees, pictures of honeycomb, wooden honey stick, or drooling honey from either is ok. Simple colors. (Designer's discretion)
Wordings:
Hex1
Product of Yemen
Header:
KORVAL /MELO/ (Brand name)
Explanatory below header
Yemen Sidr Honey from The Valley Ra'ufil (100% Pure)
(name of honey)
250g
Optional
Hex2
Pure
=
No Additives (not even natural additives)
Hex3
Raw
=
Unheated, Unpasteurized, Unprocessed honey
Hex4
Natural
=
No added color, artificial flavor, or synthetic substance
Hex5
RENOWNED
=
Very well known by honey lovers
(Natural Pure Raw and Renowned) wordings to be on a suitable place on the bottle (maybe on the cap) -
Hex6
Imported By
The Lantern Bazaar Pte Ltd
No. 317, Cobalt Ferry Road, #09-12
Cobalt Ferry Plaza
Singapore 195340
Wordings can be rearranged - its up to the designer's discretion where and how to place them and in which order.-
Designer must be willing to do numerous changes as the design develops

```html
<!DOCTYPE html>
<html lang="en">
<head>
<meta charset="utf-8">
<title>KORVAL Yemen Sidr Honey – Label Set</title>
<link href="https://fonts.googleapis.com/css2?family=Bebas+Neue&display=swap" rel="stylesheet">
<style>
  :root {
    --board: #857169;
    --cream: #fbf3e6;
    --cream-deep: #f1dcbc;
    --gold: #e3b55e;
    --gold-text: #dfa94c;
    --plaque-light: #f7e8c4;
    --plaque-dark: #d9b46e;
    --ink: #231f20;
    --white: #ffffff;
  }
  * { margin: 0; padding: 0; box-sizing: border-box; }
  html, body { width: 1200px; height: 1142px; overflow: hidden; }
  body {
    background: var(--board);
    font-family: "Bebas Neue", "Oswald", sans-serif;
    color: var(--ink);
    position: relative;
  }
  .label {
    position: absolute;
    background: radial-gradient(ellipse at 50% 45%, var(--white) 0%, var(--cream) 35%, var(--cream-deep) 100%);
    overflow: hidden;
  }
  .label--front { left: 122px; top: 205px; width: 706px; height: 415px; }
  .label--back { left: 856px; top: 205px; width: 234px; height: 415px; }
  .abs { position: absolute; white-space: nowrap; line-height: 1; }

  .plaque {
    position: absolute; left: 246px; top: 70px; width: 216px; height: 151px;
    border-radius: 8px;
    background: radial-gradient(ellipse at 50% 40%, var(--plaque-light), var(--plaque-dark));
  }
  .plaque__frame {
    position: absolute; inset: 7px; border: 1px solid #8a6a36; border-radius: 3px;
  }
  .brand-name {
    position: absolute; left: 0; right: 0; top: 44px; text-align: center;
    font-size: 46px; letter-spacing: 6px; line-height: 1; color: var(--ink);
  }
  .brand-sub {
    position: absolute; left: 0; right: 0; top: 96px; text-align: center;
    font-size: 17px; letter-spacing: 4px; color: var(--gold-text); line-height: 1;
  }
  .brand-origin {
    position: absolute; left: 0; right: 0; top: 118px; text-align: center;
    font-size: 12px; letter-spacing: 1px; color: var(--ink); line-height: 1;
  }

  .bee-mark {
    position: absolute; left: 331px; top: 248px; width: 40px; height: 40px;
    border-radius: 50%;
    background: radial-gradient(circle, var(--gold) 0%, var(--cream-deep) 75%, transparent 76%);
  }

  .heading {
    font-size: 19px; color: var(--gold-text); letter-spacing: 0.5px;
    border-bottom: 2px solid var(--gold); padding-bottom: 1px;
  }
  .claim { font-size: 19px; letter-spacing: 1px; }
  .claim--small { font-size: 16px; letter-spacing: 1.2px; }

  .name-band {
    position: absolute; left: 0; top: 332px; width: 706px; height: 35px;
    background: var(--gold); border-bottom: 2px solid #f3dfb5;
    display: flex; align-items: center; justify-content: center;
    font-size: 22px; letter-spacing: 2.5px;
  }
  .footer-note { font-size: 12px; top: 393px; }

  .back-heading { font-size: 19px; color: var(--gold-text); border-bottom: 2px solid var(--gold); padding-bottom: 1px; }
  .back-address { font-size: 15px; letter-spacing: 0.8px; line-height: 16.5px; }
  .info-panel {
    position: absolute; left: 18px; top: 201px; width: 204px; height: 174px;
    background: var(--white); border-radius: 12px;
  }

  .cap-seal { position: absolute; left: 893px; top: 741px; width: 192px; height: 192px; }
</style>
</head>
<body>

<section class="label label--front" aria-label="Front label">
  <div class="plaque">
    <div class="plaque__frame"></div>
    <div class="brand-name">KORVAL</div>
    <div class="brand-sub">YEMEN SIDR HONEY</div>
    <div class="brand-origin">FROM THE VALLEY RA'UFIL</div>
  </div>

  <div class="bee-mark" role="img" aria-label="Small honey bee emblem"></div>

  <div class="abs heading" style="left:24px;top:135px;">100% PURE</div>
  <div class="abs claim" style="left:24px;top:156px;">NO ADDITIVES</div>
  <div class="abs claim claim--small" style="left:24px;top:177px;">(NOT EVEN NATURAL ADDITIVES)</div>

  <div class="abs heading" style="left:24px;top:220px;">NATURAL</div>
  <div class="abs claim" style="left:24px;top:245px;">NO ADDED COLOR</div>
  <div class="abs claim" style="left:24px;top:264px;">NO ARTIFICIAL FLAVOR</div>
  <div class="abs claim" style="left:24px;top:283px;">NO SYNTHETIC SUBSTANCE</div>

  <div class="abs heading" style="left:492px;top:135px;">RAW</div>
  <div class="abs claim" style="left:492px;top:161px;">UNHEATED</div>
  <div class="abs claim" style="left:492px;top:181px;">UNPASTEURIZED</div>
  <div class="abs claim" style="left:492px;top:202px;">UNPROCESSED HONEY</div>

  <div class="abs heading" style="left:492px;top:244px;">RENOWNED</div>
  <div class="abs claim" style="left:492px;top:272px;">VERY WELL KNOWN</div>
  <div class="abs claim" style="left:492px;top:292px;">BY HONEY LOVERS</div>

  <div class="name-band">NAME OF THE HONEY</div>

  <div class="abs footer-note" style="left:171px;">250 GM</div>
  <div class="abs footer-note" style="left:251px;">PRODUCT OF YEMEN</div>
  <div class="abs footer-note" style="left:418px;">100% PURE</div>
</section>

<section class="label label--back" aria-label="Back label">
  <div class="abs back-heading" style="left:16px;top:96px;">IMPORTED BY</div>
  <div class="abs back-address" style="left:16px;top:124px;">
    THE LANTERN BAZAAR PTE LTD<br>
    NO. 317, COBALT FERRY ROAD,<br>
    #09-12 COBALT FERRY PLAZA<br>
    SINGAPORE 195340
  </div>
  <div class="info-panel"></div>
</section>

<svg class="cap-seal" viewBox="0 0 192 192" aria-label="Cap seal">
  <defs>
    <radialGradient id="seal-fill" cx="50%" cy="50%" r="50%">
      <stop offset="0%" stop-color="#ffffff"/>
      <stop offset="60%" stop-color="#fbf3e6"/>
      <stop offset="100%" stop-color="#f1dcbc"/>
    </radialGradient>
    <path id="seal-top" d="M 24 96 A 72 72 0 0 1 168 96"/>
    <path id="seal-bottom" d="M 18 96 A 78 78 0 0 0 174 96"/>
  </defs>
  <circle cx="96" cy="96" r="95" fill="var(--white)"/>
  <circle cx="96" cy="96" r="90" fill="url(#seal-fill)" stroke="var(--gold)" stroke-width="2"/>
  <text font-family="Bebas Neue, sans-serif" font-size="15" fill="var(--ink)" letter-spacing="1.5">
    <textPath href="#seal-top" startOffset="50%" text-anchor="middle">NATURAL.PURE.RAW.RENOWNED</textPath>
  </text>
  <text font-family="Bebas Neue, sans-serif" font-size="15" fill="var(--ink)" letter-spacing="1.5" dominant-baseline="hanging">
    <textPath href="#seal-bottom" startOffset="50%" text-anchor="middle">PRODUCT OF YEMEN. 250 GM</textPath>
  </text>
  <circle cx="96" cy="57" r="9" fill="var(--gold)" opacity="0.7" role="img" aria-label="Small honey bee emblem"/>
  <text x="96" y="107" text-anchor="middle" font-family="Bebas Neue, sans-serif" font-size="32" letter-spacing="3" fill="var(--ink)">KORVAL</text>
  <text x="96" y="122" text-anchor="middle" font-family="Bebas Neue, sans-serif" font-size="10" letter-spacing="1.5" fill="var(--gold-text)">YEMEN SIDR HONEY</text>
</svg>

</body>
</html>
```